Dr Lenora aesthetics - Grace Distilled

I need a logo design for a new aesthetics business in London. I am specialised in Botox, Dermal Fillers & Skin Pigmentation treatment. The slogan is Grace Distilled. I would like some of the writing on the card to be embossed. I would like a very elegant design with the following detail:

1. White and gray scale background. For the font colour try gold OR silver shades.
2. The business involves working on the face mostly. Anything that can be done with letter 'M'? Or any other logo?
3. The front of the card should have Dr Lenora Aesthetics and the slogan 'Grace Distilled'. The back should have my full name (Dr Lenora Brackwell), qualifications (MBBS MSC BSC), my website (www.ashfernclinicalcare.example), telephone number & email.
4. The back should also say treatments offered: ANTI-WRINKLE INJECTIONS. DERMAL FILLERS, LIP ENHANCEMENT, HYPERHYDROSIS. SKIN PIGMENTATION

Thank you very much
Updates

Project Deadline Extended
Reason: Delays in market research response. I would be grateful for an extension please. Many thanks

Target Market(s)

Female and male aged 18 and above

Industry/Entity Type

Business

Contact Information for Business Card

Elegant design. Square corners. British standard size. Horizontal design. Should contain the slogan, contact details.

Font styles to use
Script

Colors
c9c9c9
fbed22
ffffff
f5f5f5
000000

Requirements
Must have
• All that's mentioned above
Nice to have
• A logo with the outline of a female face. Or anything that can be done with the letter M of Lenora.
Should not have
• No colours like green / purple / orange

```html
<!DOCTYPE html>
<html lang="en">
<head>
<meta charset="utf-8">
<title>Dr Lenora Aesthetics – Business Card</title>
<link rel="stylesheet" href="https://fonts.googleapis.com/css2?family=Fira+Sans:wght@500&family=Jost:wght@400;500&family=Pinyon+Script&family=Arimo:wght@700&display=swap">
<style>
  :root {
    --stage: #6a6a6a;
    --card: #c9c9c9;
    --ink: #000000;
    --gold: #fbed22;
    --glow: #ffffff;
    --label: #ffffff;
  }
  * { margin: 0; padding: 0; box-sizing: border-box; }
  html, body { width: 990px; height: 1200px; overflow: hidden; }
  body {
    position: relative;
    background: radial-gradient(ellipse at center, #777777 0%, var(--stage) 70%, #5c5c5c 100%);
    font-family: "Jost", sans-serif;
    color: var(--ink);
  }
  .side-label {
    position: absolute;
    font-family: "Arimo", sans-serif;
    font-weight: 700;
    font-size: 31px;
    color: var(--label);
    line-height: 1;
  }
  .side-label--front { left: 127px; top: 26px; }
  .side-label--back { left: 831px; top: 1164px; }

  .card {
    position: absolute;
    left: 54px;
    width: 880px;
    height: 515px;
    background: var(--card);
    box-shadow: 0 8px 26px rgba(0,0,0,.55), 0 2px 6px rgba(0,0,0,.35);
  }
  .card--front { top: 71px; }
  .card--back { top: 622px; }

  .brand-mark {
    position: absolute;
    display: flex;
    align-items: center;
    gap: 8px;
    font-family: "Jost", sans-serif;
    font-weight: 500;
    color: var(--ink);
  }
  .brand-mark__dot {
    border-radius: 50%;
    background: var(--ink);
    flex: none;
  }
  .card--front .brand-mark { left: 380px; top: 130px; font-size: 34px; }
  .card--front .brand-mark__dot { width: 22px; height: 22px; }
  .card--back .brand-mark { left: 752px; top: 416px; font-size: 20px; gap: 5px; }
  .card--back .brand-mark__dot { width: 13px; height: 13px; }

  .business-name {
    position: absolute;
    left: 0; right: 0;
    top: 222px;
    text-align: center;
    font-family: "Fira Sans", sans-serif;
    font-weight: 500;
    font-size: 57px;
    line-height: 1;
    color: var(--gold);
    text-shadow: 0 0 6px var(--glow), 0 0 12px var(--glow);
  }
  .slogan {
    position: absolute;
    left: 0; right: 0;
    top: 275px;
    text-align: center;
    font-family: "Pinyon Script", cursive;
    font-size: 42px;
    line-height: 1;
    color: var(--ink);
    padding-left: 30px;
  }
  .website {
    position: absolute;
    left: 0; right: 0;
    top: 443px;
    text-align: center;
    font-size: 22px;
    color: var(--ink);
  }

  .treatments {
    position: absolute;
    left: 106px;
    top: 106px;
    font-size: 22px;
    line-height: 28px;
    list-style: none;
  }
  .practitioner {
    position: absolute;
    right: 174px;
    top: 409px;
    font-size: 21px;
    font-weight: 500;
  }
  .accent-rule {
    position: absolute;
    left: 51px;
    top: 454px;
    width: 655px;
    height: 5px;
    background: var(--gold);
  }
</style>
</head>
<body>
  <div class="side-label side-label--front">front</div>

  <section class="card card--front">
    <div class="brand-mark"><span class="brand-mark__dot"></span>Lenora</div>
    <h1 class="business-name">Dr Lenora Aesthetics</h1>
    <p class="slogan">Grace Distilled</p>
    <p class="website">www.ashfernclinicalcare.example</p>
  </section>

  <section class="card card--back">
    <ul class="treatments">
      <li>Treatments Offered:</li>
      <li>Anti-Wrinkle Injections.</li>
      <li>Dermal Fillers,</li>
      <li>Lip Enhancement,</li>
      <li>Hyperhydrosis.</li>
      <li>Skin Pigmentation</li>
    </ul>
    <p class="practitioner">Dr. Lenora Brackwell, MBBS. MSC. BSC</p>
    <div class="accent-rule"></div>
    <div class="brand-mark"><span class="brand-mark__dot"></span>Lenora</div>
  </section>

  <div class="side-label side-label--back">back</div>
</body>
</html>
```